Holiday Club Flyer for 2026

Hi Kaystudio. We need a new flyer making for our holiday club for this year. You have made the last few which have always been good. This year the theme is space so please could you change the design to a space theme. The dates of the Holiday club are 28th, 29th and 30th October. It is the same venue, same timings and same activities that happen, we need the dates updating and the them of the flyer changing to space. I have attached last years flyer for you as a reminder.

```html
<!DOCTYPE html>
<html lang="en">
<head>
<meta charset="utf-8">
<title>Space Quest Holiday Club Flyer</title>
<link href="https://fonts.googleapis.com/css2?family=Kavoon&family=Comic+Neue:wght@400;700&display=swap" rel="stylesheet">
<style>
  :root {
    --page: #e9e9e9;
    --sky: #141a44;
    --planet: #3b3f8f;
    --moon: #f2b84b;
    --title-top: #4fd1c5;
    --title-bottom: #ffd36b;
    --date-ink: #ffe7b0;
    --band: #0f8a7e;
    --ink: #f3f1ff;
    --white: #ffffff;
    --star: #fff6d8;
    --badge-red: #c8392b;
    --scene-top: #2c2f6e;
    --scene-bottom: #5a3a7a;
  }
  * { margin: 0; padding: 0; box-sizing: border-box; }
  html, body {
    width: 1200px; height: 1200px; overflow: hidden;
    background: var(--page);
  }
  .flyer {
    position: absolute; left: 203px; top: 40px;
    width: 793px; height: 1120px;
    background: var(--sky);
    overflow: hidden;
    font-family: "Comic Neue", "Comic Sans MS", cursive;
    color: var(--ink);
  }
  .backdrop { position: absolute; left: 0; top: 0; }
  .title {
    position: absolute; left: 55px; width: 700px; text-align: center;
    font-family: "Kavoon", cursive; font-weight: 400; line-height: 1;
    font-size: 104px;
  }
  .title-top { top: 72px; color: var(--title-top); }
  .title-bottom { top: 172px; color: var(--title-bottom); }
  .dates {
    position: absolute; left: 76px; top: 322px;
    font-size: 31px; line-height: 41px; color: var(--date-ink);
  }
  .times-band {
    position: absolute; left: 352px; top: 432px; width: 441px; height: 71px;
    background: var(--band); color: var(--white);
    text-align: right; padding: 11px 43px 0 0;
    font-size: 17.5px; font-weight: 700; line-height: 26px; letter-spacing: 0.5px;
  }
  .info-block {
    position: absolute; right: 43px; text-align: right;
    font-size: 16px; line-height: 20px;
  }
  .info-block strong { font-weight: 700; letter-spacing: 0.5px; }
  .location { top: 510px; }
  .register { top: 590px; }
  .details {
    position: absolute; left: 72px; top: 631px;
    font-size: 16px; line-height: 19px;
  }
  .details p + p { margin-top: 19px; }
  .age-badge { position: absolute; left: 392px; top: 647px; }
  .age-text {
    position: absolute; left: 426px; top: 680px; width: 242px;
    text-align: center; color: var(--white);
    font-size: 25px; line-height: 32px; letter-spacing: 0.5px;
  }
</style>
</head>
<body>
<main class="flyer">
  <svg class="backdrop" width="793" height="1120" viewBox="0 0 793 1120">
    <defs>
      <linearGradient id="sceneFade" x1="0" y1="0" x2="0" y2="1">
        <stop offset="0" stop-color="var(--scene-top)"/>
        <stop offset="1" stop-color="var(--scene-bottom)"/>
      </linearGradient>
    </defs>
    <circle class="planet" cx="350" cy="175" r="176" fill="var(--planet)"/>
    <circle class="moon" cx="106" cy="445" r="146" fill="var(--moon)" opacity="0.35"/>
    <g class="stars" fill="var(--star)">
      <circle cx="40" cy="60" r="3"/>
      <circle cx="120" cy="150" r="2"/>
      <circle cx="30" cy="250" r="2.5"/>
      <circle cx="640" cy="50" r="3"/>
      <circle cx="740" cy="130" r="2"/>
      <circle cx="700" cy="250" r="3"/>
      <circle cx="760" cy="360" r="2"/>
      <circle cx="600" cy="380" r="2.5"/>
      <circle cx="300" cy="560" r="2"/>
      <circle cx="40" cy="760" r="2.5"/>
      <circle cx="330" cy="790" r="2"/>
      <circle cx="750" cy="700" r="2.5"/>
    </g>
    <rect role="img" aria-label="Space scene illustration with two smiling child astronauts on a rocky moon surface, a rocket and distant planets"
      x="0" y="860" width="793" height="260" fill="url(#sceneFade)"/>
  </svg>

  <h1>
    <span class="title title-top">Space</span>
    <span class="title title-bottom">Quest</span>
  </h1>

  <p class="dates">28th, 29th<br>30th October</p>

  <div class="times-band">
    DROP OFF FROM: 8:45 AM<br>
    COLLECT YOUR CHILDREN: 12:30 PM
  </div>

  <div class="info-block location">
    <strong>LOCATION</strong><br>
    HILLTOP CHURCH ASHFORD<br>
    Meadow Lane
  </div>

  <div class="info-block register">
    <strong>REGISTER AT</strong><br>
    https://hilltop.church/holiday-club
  </div>

  <div class="details">
    <p>Featuring games, bible stories,<br>quizzes, craft &amp; more!<br>Picnic lunch is included</p>
    <p>Find Us:<br>HILLTOP CHURCH ASHFORD,<br>MEADOW LANE, ASHFORD, AB1 2CD</p>
    <p>sam@hilltopchurch.org</p>
  </div>

  <svg class="age-badge" width="311" height="196" viewBox="0 0 311 196">
    <path d="M20 10 C90 -5 220 20 290 15 C320 40 300 90 285 130 C270 175 230 196 170 185 C120 175 70 190 40 160 C10 130 40 95 15 60 C0 40 5 20 20 10 Z"
      fill="var(--badge-red)"/>
  </svg>
  <p class="age-text">RECEPTION<br>TO<br>YEAR 6</p>
</main>
</body>
</html>
```